Awesome ecommerce store banner needed!

We need a sharp, clear, strong banner for one of our subcategory pages on http://www.brivelloop.example
We'd like to incorporate the following image. We'd like the background to be gray or black. We are replacing the Wireless Intercoms banner that is orange (we hate it).
WE do like our other banners, however, so please use them as reference:
SIze: 980 x 380
Two raw images of the intercom we'd like you to encorporate have been included. Choose one or the other depending on what you think would be best. If using the single angle, please duplicate it. We want two intercoms in the banner
Simple and Clean is key:
Text: Wireless Intercoms
Text Color: Can be white/off gray
Text Style: Please keep it clean in line with the website
Background: Black/gray/white

```html
<!DOCTYPE html>
<html lang="en">
<head>
<meta charset="utf-8">
<title>Brivelloop – Wireless Intercom Systems</title>
<link rel="stylesheet" href="https://fonts.googleapis.com/css2?family=Open+Sans:wght@400;600;700;800&family=Archivo:wght@700;800;900&family=Archivo+Narrow:wght@700&display=swap">
<style>
:root{
  --orange:#e8731e;
  --orange-dark:#c9571a;
  --ink:#222;
  --ink-soft:#444;
  --muted:#777;
  --nav-top:#3d3d3d;
  --nav-bottom:#151515;
  --sidebar:#f1f1f1;
  --rule:#c8c8c8;
  --price:#e0101a;
  --banner-yellow:#f7c326;
  --white:#fff;
}
*{box-sizing:border-box;margin:0;padding:0}
html,body{width:1200px;height:1095px;overflow:hidden;background:#fff}
body{font-family:Arial,"Helvetica Neue",Helvetica,sans-serif;color:var(--ink)}
.page{position:relative;width:1028px;height:938px;transform:scale(1.1673);transform-origin:0 0;
  background:linear-gradient(#e4e4e4 0,#f4f4f4 140px,#f4f4f4 460px,#fff 460px)}
.abs{position:absolute}

/* header */
.brand{left:22px;top:28px;display:flex;align-items:center;gap:10px}
.brand-dot{width:48px;height:48px;border-radius:50%;background:var(--orange)}
.brand-name{font-family:"Archivo",sans-serif;font-weight:900;font-size:50px;color:#333;letter-spacing:-1px;line-height:1}
.toplinks{right:185px;top:6px;display:flex;font-size:12.5px;font-weight:700;color:#333}
.toplinks span{padding:0 10px;border-left:1px solid #aaa}
.toplinks span:first-child{border-left:0}
.cart{left:868px;top:0;width:50px;height:30px;background:var(--orange-dark);border-radius:0 0 4px 4px;display:flex;align-items:center;justify-content:center}
.cart-label{left:921px;top:7px;font-size:13px;font-weight:700;color:#333}
.callus{left:771px;top:46px;font-family:"Open Sans",sans-serif;font-size:19px;color:#444;line-height:1}
.callus b{font-size:24px;font-weight:700}
.hours{left:771px;top:67px;font-family:"Open Sans",sans-serif;font-size:15px;color:#777;letter-spacing:.3px}

/* nav */
.nav{left:20px;top:98px;width:981px;height:40px;background:linear-gradient(var(--nav-top),var(--nav-bottom));display:flex;align-items:center}
.nav-item{height:40px;display:flex;align-items:center;gap:6px;padding:0 18px 0 20px;color:var(--white);font-family:"Open Sans",sans-serif;font-size:17.5px;font-weight:600;border-right:1px solid #555;white-space:nowrap}
.nav-item:nth-child(3){border-right:0}
.search{position:absolute;left:630px;top:6px;width:346px;height:28px;background:var(--white);border-radius:2px}
.search-placeholder{position:absolute;left:11px;top:7px;font-size:11px;color:#999}
.search-btn{position:absolute;right:0;top:0;width:87px;height:28px;background:linear-gradient(#f4f4f4,#d8d8d8);font-family:"Open Sans",sans-serif;font-weight:700;font-size:15px;color:#333;display:flex;align-items:center;justify-content:center;gap:3px}
.search-btn i{font-style:normal;color:var(--orange)}

/* sidebar */
.content{left:20px;top:140px;width:981px;height:798px;background:var(--white)}
.sidebar{left:20px;top:168px;width:214px;height:770px;background:var(--sidebar)}
.side-title{left:36px;top:178px;font-family:"Open Sans",sans-serif;font-weight:700;font-size:20px;color:var(--orange)}
.side-list{left:38px;top:229px;width:192px;list-style:none}
.side-list li{position:relative;padding-left:8px;font-size:11.5px;font-weight:700;line-height:14px;margin-bottom:10px;color:#111}
.side-list li::before{content:"";position:absolute;left:0;top:50%;width:3px;height:3px;background:var(--orange)}
.shop-cta{width:214px;left:20px;text-align:center;font-family:"Open Sans",sans-serif;line-height:1}
.shop-cta .or{font-size:17px;color:var(--orange);font-weight:700}
.shop-cta .or b{font-size:21px}
.shop-cta .dest{font-size:19px;font-weight:700;color:#222}
.shop-cta .dest.big{font-size:24px}
.shop-cta .dest i{font-style:normal;color:var(--orange)}
.side-rule{left:20px;top:571px;width:214px;border-top:1px solid #d6d6d6}
.testi-title{left:20px;width:214px;top:623px;text-align:center;font-family:"Open Sans",sans-serif;font-weight:600;font-size:16px}
.testi-text{left:31px;top:652px;width:196px;font-size:12px;line-height:14px;color:#111}
.testi-more{left:31px;top:759px;font-size:10.5px;color:var(--orange)}
.testi-name{left:31px;top:781px;font-size:12px;font-style:italic;color:#111}

/* main */
.crumbs{left:256px;top:168px;font-size:12.5px;color:#222}
.crumbs .current{color:var(--orange);font-weight:700}
.page-title{left:256px;top:192px;font-size:15.5px;font-weight:700;color:#222}
.title-rule{left:256px;top:216px;width:725px;border-top:1px solid #999}

.banner{left:253px;top:252px;width:729px;height:281px;background:radial-gradient(ellipse at 72% 45%,#8a8a8a 0,#4a4a4a 45%,#2b2b2b 100%);overflow:hidden}
.banner-product{position:absolute;left:405px;top:12px;width:290px;height:228px;background:linear-gradient(135deg,#cfcfcf,#8c8c8c 55%,#1e1e1e);border-radius:8px;opacity:.9}
.banner-text{position:absolute;left:47px;top:92px;width:345px;font-family:"Archivo Narrow","Arial Narrow",sans-serif;font-weight:700;font-size:58px;line-height:55px;letter-spacing:.5px;white-space:nowrap}
.banner-text .w{color:var(--white)}
.banner-text .y{color:var(--banner-yellow)}

.card{width:175px;height:260px;background:var(--white);border:1px solid #c4c4c4}
.card-img{position:absolute;left:30px;top:18px;width:112px;height:100px;background:linear-gradient(135deg,#bcbcbc,#3b3b3b)}
.card-name{position:absolute;left:5px;top:148px;width:166px;font-size:12px;font-weight:700;line-height:14px;color:#111}
.card-reg{position:absolute;left:5px;top:194px;font-size:9.5px;color:#888}
.card-reg s{color:#888}
.card-price{position:absolute;left:5px;top:206px;font-size:12px;font-weight:700;color:#111}
.card-price b{color:var(--price)}
.card-btn{position:absolute;left:38px;top:230px;width:97px;height:22px;background:linear-gradient(#fafafa,#d6d6d6);border-radius:3px;font-family:"Open Sans",sans-serif;font-size:13px;font-weight:600;color:#333;display:flex;align-items:center;justify-content:center;gap:3px}
.card-btn i{font-style:normal;color:var(--orange);font-weight:800}
.flag{position:absolute;left:-4px;top:-4px;height:22px;padding:0 26px 0 8px;color:var(--white);font-family:"Open Sans",sans-serif;font-size:13.5px;font-weight:600;display:flex;align-items:center;gap:6px;clip-path:polygon(0 0,100% 0,88% 100%,0 100%)}
.flag.pick{background:var(--orange)}
.flag.sale{background:#c7261d}
.flag-dot{width:12px;height:12px;border-radius:50%;background:var(--white);opacity:.85}
</style>
</head>
<body>
<div class="page">

  <header>
    <div class="abs brand"><span class="brand-dot"></span><span class="brand-name">Brivelloop</span></div>
    <nav class="abs toplinks"><span>Home</span><span>About</span><span>Contact</span></nav>
    <div class="abs cart">
      <svg width="26" height="20" viewBox="0 0 26 20" fill="none" stroke="#fff" stroke-width="2.2"><path d="M1 2h4l3 11h13l3-8H7"/><circle cx="10" cy="17" r="1.6" fill="#fff"/><circle cx="19" cy="17" r="1.6" fill="#fff"/></svg>
    </div>
    <div class="abs cart-label">YOUR CART</div>
    <div class="abs callus">Call Us <b>555.014.2290</b></div>
    <div class="abs hours">Monday-Friday 7am-3pm PST</div>
  </header>

  <div class="abs nav">
    <div class="nav-item">Shop Home Automation <svg width="16" height="10" viewBox="0 0 16 10"><path d="M2 2l6 6 6-6" stroke="#fff" stroke-width="3" fill="none"/></svg></div>
    <div class="nav-item">Shop Cool Gadgets <svg width="16" height="10" viewBox="0 0 16 10"><path d="M2 2l6 6 6-6" stroke="#fff" stroke-width="3" fill="none"/></svg></div>
    <div class="nav-item">Top Sellers</div>
    <div class="search"><span class="search-placeholder">Enter Keyword or Item#</span><span class="search-btn">SEARCH<i>›</i></span></div>
  </div>

  <div class="abs content"></div>

  <aside>
    <div class="abs sidebar"></div>
    <div class="abs side-title">Home Automation</div>
    <ul class="abs side-list">
      <li>Wireless Driveway Alarm Systems &amp; Outdoor Motion Detectors</li>
      <li>Wireless Doorbell Systems</li>
      <li>Indoor Motion Sensors</li>
      <li>Remote Light Switches &amp; Wireless Power Outlet Triggers</li>
    </ul>
    <div class="abs shop-cta" style="top:390px"><div class="or">or <b>SHOP</b></div><div class="dest">Home Automation<i>›</i></div></div>
    <div class="abs shop-cta" style="top:474px"><div class="or">or <b>SHOP</b></div><div class="dest big">Cool Gadgets<i>›</i></div></div>
    <div class="abs side-rule"></div>
    <div class="abs testi-title">Customer Testimonials</div>
    <p class="abs testi-text">"I found this experience very easy. There were no delays. The package arrived in a short time with no damage. I felt like I was their only customer. Brivelloop made me feel as if I was a major purchaser. They are great."</p>
    <div class="abs testi-more">READ MORE</div>
    <div class="abs testi-name">Daniel R. (Pine Hollow, ID)</div>
  </aside>

  <main>
    <div class="abs crumbs">Home &gt; View All Categories... &gt; <span class="current">Wireless Intercom Systems</span></div>
    <h1 class="abs page-title">Wireless Intercom Systems</h1>
    <div class="abs title-rule"></div>

    <section class="abs banner">
      <div class="banner-product" role="img" aria-label="Two silver and black wireless intercom units with antennas"></div>
      <div class="banner-text"><div class="w">WIRELESS</div><div class="y">INTERCOMS</div></div>
    </section>

    <article class="abs card" style="left:256px;top:570px">
      <div class="card-img" role="img" aria-label="Pair of portable silver wireless intercoms"></div>
      <div class="card-name">Portable Wireless Intercom System Set</div>
      <div class="card-reg">Regular Price <s>$148.00</s></div>
      <div class="card-price">Our Price: <b>$119.00</b></div>
      <div class="card-btn"><i>›</i>More Info</div>
    </article>

    <article class="abs card" style="left:439px;top:570px">
      <div class="card-img" role="img" aria-label="Two black base station intercoms with antennas"></div>
      <div class="flag pick"><span class="flag-dot"></span>staff pick</div>
      <div class="card-name">MURS 4-Mile Range Intercom Set: Base Stations by Norvane Alert</div>
      <div class="card-reg">Regular Price <s>$249.00</s></div>
      <div class="card-price">Our Price: <b>$158.00</b></div>
      <div class="card-btn"><i>›</i>More Info</div>
    </article>

    <article class="abs card" style="left:622px;top:570px">
      <div class="card-img" role="img" aria-label="Two black desktop intercom units"></div>
      <div class="card-name">Basic 3-Channel Intercom System Set</div>
      <div class="card-price">Our Price: <b>$59.00</b></div>
      <div class="card-btn"><i>›</i>More Info</div>
    </article>

    <article class="abs card" style="left:805px;top:570px">
      <div class="card-img" role="img" aria-label="White doorbell button with silver intercom base"></div>
      <div class="flag sale"><span class="flag-dot"></span>on sale</div>
      <div class="card-name">Wireless Doorbell w/ Intercom</div>
      <div class="card-reg">Regular Price <s>$179.00</s></div>
      <div class="card-price">Our Price: <b>$139.00</b></div>
      <div class="card-btn"><i>›</i>More Info</div>
    </article>

    <article class="abs card" style="left:256px;top:850px"><div class="card-img" role="img" aria-label="Pair of handheld radios"></div></article>
    <article class="abs card" style="left:439px;top:850px"><div class="card-img" role="img" aria-label="Black intercom base stations"></div></article>
    <article class="abs card" style="left:622px;top:850px"><div class="card-img" role="img" aria-label="Black handheld intercom unit"></div></article>
    <article class="abs card" style="left:805px;top:850px"><div class="card-img" role="img" aria-label="Yellow call box unit with antenna"></div></article>
  </main>

</div>
</body>
</html>
```